KR Iron Designworks, Inc.

I'm looking for business card design for an existing company with an existing logo/website. www.kriron-designworks.example. VETERAN OWNED logo must be present.

Target Market(s)

Structural and architectural steel fabricators

Industry/Entity Type

Structural and architectural steel detailing and engineering

Contact Information for Business Card

logo, business name, address, phone, website, email, employee info

Font styles to use
Serif

Colors
00AB8E
00BBA5
67D7C9
C6EFE9
E9F9F6

Requirements
Must have
• company logo, website, VETERAN OWNED LOGO
Should not have
• Don't make it too busy. Less is more

```html
<!DOCTYPE html>
<html lang="en">
<head>
<meta charset="utf-8">
<title>KR Iron Designworks – Business Card</title>
<link rel="stylesheet" href="https://fonts.googleapis.com/css2?family=Orbitron:wght@900&family=Arimo:wght@400;700&display=swap">
<style>
  :root {
    --stage: #3a3b3d;
    --card-white: #ffffff;
    --card-black: #161616;
    --teal-dark: #00ab8e;
    --teal: #00bba5;
    --teal-light: #67d7c9;
    --teal-pale: #c6efe9;
    --teal-mist: #e9f9f6;
    --ink: #111111;
    --text-grey: #3d3d3d;
    --steel-grey: #6b6f73;
    --badge-neutral: #5a5c60;
  }
  * { box-sizing: border-box; margin: 0; padding: 0; }
  html, body { width: 1200px; height: 982px; overflow: hidden; }
  body { background: var(--stage); position: relative; font-family: "Arimo", Arial, sans-serif; }

  .card {
    position: absolute;
    left: 250px;
    width: 700px;
    height: 400px;
    border-radius: 22px;
    overflow: hidden;
    box-shadow: 0 10px 30px rgba(0,0,0,.45);
  }

  /* Back */
  .card-back { top: 50px; background: var(--card-black); }
  .mark-pattern {
    position: absolute; inset: 0;
    background: linear-gradient(115deg, #4a4a4a 0%, #262626 30%, #121212 60%, #0b0b0b 100%);
  }
  .veteran-badge {
    position: absolute; left: 160px; top: 170px;
    width: 210px; height: 60px;
    background: var(--badge-neutral);
    border-radius: 8px;
  }
  .back-brand {
    position: absolute; right: 60px; bottom: 70px;
    display: flex; align-items: center; gap: 10px;
    font-weight: 700; font-size: 16px;
    letter-spacing: 1px; color: var(--teal);
  }
  .back-brand .dot { width: 16px; height: 16px; background: var(--teal); }

  /* Front */
  .card-front { top: 520px; background: var(--card-white); }
  .name-band {
    position: absolute; left: 0; top: 40px; width: 450px; height: 120px;
    background: linear-gradient(100deg, var(--teal-dark) 0%, var(--teal-light) 35%, var(--teal) 55%, var(--teal-pale) 72%, var(--teal-dark) 100%);
  }
  .person-name {
    position: absolute; left: 40px; top: 66px;
    font-family: "Orbitron", sans-serif; font-weight: 900; font-size: 34px;
    letter-spacing: 2px; color: var(--ink);
  }
  .person-title {
    position: absolute; left: 40px; top: 112px;
    font-size: 19px; color: var(--ink);
  }
  .steel-strip {
    position: absolute; right: 0; top: 150px; width: 110px; height: 110px;
    background: linear-gradient(90deg, #f4f4f4, #8d9196 50%, #5e6166);
  }
  .brand {
    position: absolute; right: 130px; top: 178px;
    display: flex; align-items: center; gap: 12px;
    font-weight: 700; font-size: 22px; letter-spacing: 1px; color: var(--steel-grey);
  }
  .brand .dot { width: 22px; height: 22px; background: var(--teal); }

  .contact {
    position: absolute; left: 40px; bottom: 50px;
    list-style: none; font-size: 19px; color: var(--text-grey);
  }
  .contact li { display: flex; align-items: center; gap: 12px; line-height: 30px; }
  .contact svg { width: 16px; height: 16px; fill: var(--teal); flex: none; }

  .address {
    position: absolute; right: 40px; bottom: 40px;
    text-align: right; font-size: 19px; line-height: 28px; color: var(--text-grey);
    font-style: normal;
  }
  .address .company { color: var(--teal); font-weight: 700; }
</style>
</head>
<body>

<section class="card card-back">
  <div class="mark-pattern" role="img" aria-label="Tone-on-tone repeated company mark pattern in graphite and black"></div>
  <div class="veteran-badge" role="img" aria-label="Veteran owned business badge"></div>
  <div class="back-brand"><span class="dot"></span>KR IRON DESIGNWORKS</div>
</section>

<section class="card card-front">
  <div class="name-band"></div>
  <h1 class="person-name">EVAN MARLOWE</h1>
  <p class="person-title">Founder &amp; CEO</p>

  <div class="steel-strip"></div>
  <div class="brand"><span class="dot"></span>KR IRON DESIGNWORKS</div>

  <ul class="contact">
    <li>
      <svg viewBox="0 0 16 16"><path d="M3.5 1l3 3-1.6 1.8a9 9 0 0 0 5.3 5.3L12 9.5l3 3-2 2.5C7 15 1 9 1 3z"/></svg>
      555.014.2287
    </li>
    <li>
      <svg viewBox="0 0 16 16"><path d="M1 3h14v10H1z M1 3l7 6 7-6" stroke="#fff" stroke-width="1.2"/></svg>
      sales@kriron-designworks.example
    </li>
    <li>
      <svg viewBox="0 0 16 16"><circle cx="8" cy="8" r="7"/><path d="M1 8h14M8 1c3 3 3 11 0 14M8 1c-3 3-3 11 0 14" stroke="#fff" stroke-width="1" fill="none"/></svg>
      www.kriron-designworks.example
    </li>
  </ul>

  <address class="address">
    <span class="company">KR Iron Designworks, Inc.</span><br>
    410 Harbor Mill Rd, Ste 120<br>
    Riverton, FL 30000
  </address>
</section>

</body>
</html>
```